Volora Laundry and Dry Cleaning Poster

We need a Poster and Window Sticker for our Laundry and Dry cleaning shop (VOLORA LAUNDRY AND DRY CLEANING).
info we like on the design. Logo is included
Company Name: Volora Laundry and Dry Cleaning
Slogan: It Comes Back Clean
Location: Kwentu-Dasor, Accra
Working Hours: Mon-Sat 8am to 5pm
Tel: +233 30 781 6242
email:info@voloralaundry.example
website: www.voloralaundry.example
fb: fb.com/voloralaundry

Target Market(s)

Laundry Shop

Colors
33a6d7
9bcb3b

```html
<!DOCTYPE html>
<html lang="en">
<head>
<meta charset="utf-8">
<title>Volora Laundry and Dry Cleaning Poster</title>
<link href="https://fonts.googleapis.com/css2?family=Open+Sans:ital,wght@0,600;1,800&family=Roboto+Condensed:wght@500&display=swap" rel="stylesheet">
<style>
  :root {
    --brand-blue: #33a6d7;
    --deep-blue: #0f5fa8;
    --brand-green: #9bcb3b;
    --bar-green: #14733a;
    --page-bg: #e6e7e9;
    --white: #ffffff;
    --photo-light: #e9ecee;
    --photo-mid: #b9c2c7;
  }
  * { margin: 0; padding: 0; box-sizing: border-box; }
  html, body { width: 797px; height: 1200px; overflow: hidden; background: var(--page-bg); }
  .poster {
    position: absolute; left: 18px; top: 277px;
    width: 760px; height: 646px;
    background: var(--white); overflow: hidden;
    box-shadow: 0 2px 6px rgba(0,0,0,.18);
    font-family: "Open Sans", Arial, sans-serif;
  }
  .poster__art { position: absolute; inset: 0; }
  .brand { position: absolute; left: 42px; top: 45px; display: flex; align-items: center; gap: 10px; color: var(--brand-blue); }
  .brand__dot { width: 78px; height: 78px; border-radius: 50%; background: var(--brand-blue); flex: none; }
  .brand__text { font-weight: 600; }
  .brand__name { font-size: 56px; line-height: 56px; letter-spacing: -1px; }
  .brand__line { font-size: 9.5px; letter-spacing: .2px; margin-top: 4px; }
  .slogan { position: absolute; left: 0; top: 0; color: var(--white); font-style: italic; font-weight: 800; }
  .slogan span { position: absolute; white-space: nowrap; line-height: 1; }
  .slogan__first { left: 56px; top: 236px; font-size: 52px; }
  .slogan__second { left: 160px; top: 285px; font-size: 56px; }
  .slogan__third { left: 45px; top: 315px; font-size: 92px; letter-spacing: -1px; }
  .contact { position: absolute; left: 0; top: 414px; list-style: none; }
  .contact li {
    width: 340px; height: 32px; margin-bottom: 12px;
    padding-left: 47px; background: var(--bar-green);
    color: var(--white); font-family: "Roboto Condensed", Arial, sans-serif;
    font-weight: 500; font-size: 24px; line-height: 32px; opacity: .93;
  }
  .web {
    position: absolute; left: 390px; top: 579px; width: 370px; height: 44px;
    background: rgba(155,203,59,.92); color: var(--white);
    font-family: "Roboto Condensed", Arial, sans-serif; font-weight: 500;
    font-size: 26px; line-height: 44px; padding-left: 16px; letter-spacing: .3px;
  }
</style>
</head>
<body>
<main class="poster">
  <svg class="poster__art" viewBox="0 0 760 646" width="760" height="646">
    <defs>
      <linearGradient id="photoTone" x1="0" y1="0" x2="1" y2="1">
        <stop offset="0" stop-color="var(--photo-light)"/>
        <stop offset=".6" stop-color="var(--photo-mid)"/>
        <stop offset="1" stop-color="#6f7c86"/>
      </linearGradient>
      <linearGradient id="circleTone" x1="0" y1="0" x2="1" y2="1">
        <stop offset="0" stop-color="var(--deep-blue)"/>
        <stop offset=".55" stop-color="#1f86c4"/>
        <stop offset="1" stop-color="#25a0c8"/>
      </linearGradient>
    </defs>
    <path class="photo-area" role="img" aria-label="Photo: a smiling man pours detergent into a washing machine in a bright laundromat, a woman loads a dryer behind him"
          d="M760 40 C610 10 420 20 290 150 L240 646 L760 646 Z" fill="url(#photoTone)"/>
    <path class="arc-top" d="M330 60 C480 0 650 5 760 55 L760 75 C650 30 480 25 330 60 Z" fill="var(--brand-green)"/>
    <path class="arc-left" d="M0 190 C120 130 300 150 390 230" fill="none" stroke="var(--brand-green)" stroke-width="3"/>
    <path class="arc-left-band" d="M0 235 C110 170 300 175 395 270 L395 300 C300 205 110 195 0 255 Z" fill="var(--brand-green)"/>
    <ellipse class="blue-circle" cx="150" cy="470" rx="245" ry="272" fill="url(#circleTone)" opacity=".95"/>
    <ellipse cx="150" cy="470" rx="245" ry="272" fill="none" stroke="var(--white)" stroke-width="3"/>
  </svg>

  <div class="brand">
    <div class="brand__dot"></div>
    <div class="brand__text">
      <div class="brand__name">Volora</div>
      <div class="brand__line">LAUNDRY AND DRY CLEANING</div>
    </div>
  </div>

  <h1 class="slogan">
    <span class="slogan__first">It Comes</span>
    <span class="slogan__second">Back</span>
    <span class="slogan__third">Clean</span>
  </h1>

  <ul class="contact">
    <li>Kwentu-Dasor, Accra</li>
    <li>Mon-Sat 8am to 5pm</li>
    <li>info@voloralaundry.example</li>
    <li>+233 30 781 6242</li>
    <li>fb.com/voloralaundry</li>
  </ul>

  <div class="web">www.voloralaundry.example</div>
</main>
</body>
</html>
```